Barbados hotel and property development company needs new corporate PowerPoint deck design

We need a new corporate PowerPoint deck for harborline holdings - a Barbados based company who operate and develop a hotel called the heron (https://www.theheronbay.example/)
We need a professional deck we can use across our organisation to interact with investors and property buyers. This deck needs placeholder / slide types to present financial and text tables, s well as graphs and charts

Target Market(s)

Investors, property buyers and corporate audience

Industry/Entity Type

Hospitality and tourism

Colors
0054AA
0677BA
7BADD7
CADEEF
E8F1F8
0094D4
00A9DD
6FCCEA
C7EBF8
E9F6FB

Requirements
Must have
• Follow our blue based design and graphic principles per or website
Nice to have
• We’ve got lots of high res pictures of our beach, rooms and property on the website. We would like to use these as page breaks and divider slides in our deck

```html
<!DOCTYPE html>
<html lang="en">
<head>
<meta charset="utf-8">
<title>The Heron – Corporate Deck</title>
<link rel="stylesheet" href="https://fonts.googleapis.com/css2?family=Jost:wght@400;500&family=Roboto:wght@400;500;700&display=swap">
<style>
:root{
  --navy:#0b5a8c;
  --blue:#0677ba;
  --mid:#2a8fcf;
  --sky:#58b0e0;
  --pale:#9dd3ef;
  --ice:#c7ebf8;
  --canvas:#e4f3fb;
  --ink:#1b1b1b;
  --text:#4a4a4a;
  --rule:#e2e2e2;
}
*{margin:0;padding:0;box-sizing:border-box}
html,body{width:1200px;height:4051px;overflow:hidden}
body{background:var(--canvas);font-family:"Roboto",sans-serif;color:var(--ink);position:relative}
.slide{position:absolute;left:76px;width:1048px;height:588px;background:#fff;box-shadow:0 4px 18px rgba(20,80,120,.12);overflow:hidden}
.slide-title{position:absolute;left:58px;top:32px;font-family:"Jost",sans-serif;font-weight:400;font-size:33px;letter-spacing:.5px;color:var(--ink);text-transform:uppercase}
.title-marker{position:absolute;left:0;top:39px;width:0;height:0;border-top:13px solid transparent;border-bottom:13px solid transparent;border-left:22px solid var(--blue)}
/* footer */
.footer{position:absolute;left:0;bottom:0;width:100%;height:36px;background:var(--navy);color:#fff;font-size:10px}
.footer .brand{position:absolute;left:61px;top:0;width:147px;height:36px;background:#fff;display:flex;align-items:center;justify-content:center;font-family:"Jost",sans-serif;font-size:20px;color:var(--navy)}
.footer.light{background:#fff;color:#333}
.footer.light .brand{background:var(--navy);color:#fff}
.contact{position:absolute;top:0;height:36px;display:flex;align-items:center;gap:5px;white-space:nowrap}
.contact svg{width:9px;height:9px;fill:currentColor}
.sep{position:absolute;top:13px;width:1px;height:10px;background:currentColor;opacity:.7}
.page-label{position:absolute;left:923px;top:0;line-height:36px}
.page-div{position:absolute;left:959px;top:8px;width:1px;height:20px;background:currentColor;opacity:.6}
.page-num{position:absolute;left:975px;top:0;line-height:36px}
.footer.light .page-num{color:var(--blue)}
/* hero */
.hero{position:absolute;left:0;top:0;width:100%;height:552px;background:linear-gradient(180deg,#eef1f4 0%,#d9e3ea 28%,#7fa7b8 45%,#3f7f96 55%,#4f7a4a 70%,#3e5a32 85%,#5a5a48 100%)}
.hero-title{position:absolute;left:0;width:100%;top:78px;text-align:center;font-family:"Jost",sans-serif;font-size:39px;line-height:56px;color:#111;text-transform:uppercase}
.hero-rule{position:absolute;left:501px;top:184px;width:46px;height:3px;background:var(--navy)}
.hero-copy{position:absolute;left:224px;top:207px;width:600px;text-align:center;font-size:15px;line-height:26px;color:#111}
/* graph */
.chart-svg{position:absolute;left:0;top:0}
.side-head{position:absolute;left:651px;top:189px;font-family:"Jost",sans-serif;font-size:21px;line-height:30px;color:var(--ink);text-transform:uppercase}
.side-head span{border-bottom:2px solid var(--navy)}
.side-copy{position:absolute;left:651px;top:260px;width:340px;font-size:12.4px;line-height:21.8px;color:var(--text)}
/* list */
.legend-item{position:absolute;left:489px;width:520px;height:80px}
.legend-icon{position:absolute;left:0;top:0;width:70px;height:70px;border-radius:50%;border:5px solid #fff;box-shadow:0 3px 10px rgba(0,80,140,.25);display:flex;align-items:center;justify-content:center}
.legend-icon svg{width:30px;height:30px;fill:none;stroke:#fff;stroke-width:2}
.legend-item h3{position:absolute;left:98px;top:4px;font-weight:500;font-size:15.5px;color:var(--ink)}
.legend-item p{position:absolute;left:98px;top:30px;width:420px;font-size:12.4px;line-height:19px;color:var(--text)}
/* table */
.data-table{position:absolute;left:226px;top:131px;width:597px;border-collapse:collapse;font-size:9.5px}
.data-table th{height:36px;color:#fff;font-weight:700;font-size:12px;text-align:center}
.data-table th:first-child{text-align:left;padding-left:15px;background:var(--navy)}
.data-table th:nth-child(2){background:#1f88c8}
.data-table th:nth-child(3){background:var(--sky)}
.data-table th:nth-child(4){background:#a8d8f2}
.data-table td{height:32px;border:1px solid var(--rule);text-align:center;color:#222}
.data-table td:first-child{text-align:left;padding-left:15px;font-weight:500}
.data-table tr:nth-child(even) td{background:#f7f7f7}
/* gallery */
.photo{position:absolute;width:288px;height:190px}
/* occasions */
.feature-photo{position:absolute;left:61px;top:126px;width:463px;height:354px;background:linear-gradient(180deg,#5f8a4d 0%,#8fb3a5 35%,#b9d4d9 50%,#4fb1bf 70%,#2e9eb0 100%)}
.features{position:absolute;left:569px;top:172px;width:420px;list-style:none;font-size:13px;line-height:20.5px;color:var(--text)}
.features li{position:relative;padding-left:20px;margin-bottom:8px}
.features li::before{content:"»";position:absolute;left:0;top:-1px;color:var(--blue);font-size:15px}
</style>
</head>
<body>

<!-- Slide 1: cover -->
<section class="slide" style="top:88px">
  <div class="hero" role="img" aria-label="Resort terraces with palm gardens and a lagoon pool overlooking the ocean"></div>
  <h1 class="hero-title">When you get here,<br>you’ll know</h1>
  <div class="hero-rule"></div>
  <p class="hero-copy">The Heron Resort seamlessly combines historic architectural design with world-class amenities and services in a spectacular setting overlooking one of the world's best beaches.</p>
  <footer class="footer light">
    <div class="brand">The Heron</div>
    <div class="contact" style="left:310px"><svg viewBox="0 0 10 10"><path d="M2 0l2 2-1 1.5c.8 1.6 2 2.8 3.5 3.5L8 6l2 2-1.5 2C4 9.5.5 6 0 1.5z"/></svg>(246) 555-0142</div>
    <div class="sep" style="left:408px"></div>
    <div class="contact" style="left:423px"><svg viewBox="0 0 10 10"><path d="M0 2h10v6H0z M0 2l5 3.5L10 2" stroke="#fff" stroke-width=".8"/></svg>reservations@theheronbay.example</div>
    <div class="sep" style="left:581px"></div>
    <div class="contact" style="left:595px"><svg viewBox="0 0 10 10"><circle cx="5" cy="5" r="5"/></svg>https://www.theheronbay.example/</div>
    <div class="page-label">Page</div><div class="page-div"></div><div class="page-num">01</div>
  </footer>
</section>

<!-- Slide 2: graphs -->
<section class="slide" style="top:745px">
  <div class="title-marker"></div>
  <h2 class="slide-title">Financial Graphs</h2>
  <svg class="chart-svg" width="640" height="500" viewBox="0 0 640 500" font-family="Roboto, sans-serif" font-size="11">
    <g stroke="#e6e6e6" fill="none">
      <rect x="90" y="134" width="527" height="325"/>
      <line x1="165" y1="134" x2="165" y2="459"/><line x1="240" y1="134" x2="240" y2="459"/>
      <line x1="316" y1="134" x2="316" y2="459"/><line x1="391" y1="134" x2="391" y2="459"/>
      <line x1="466" y1="134" x2="466" y2="459"/><line x1="541" y1="134" x2="541" y2="459"/>
    </g>
    <g fill="#333" text-anchor="end">
      <text x="78" y="138">120</text><text x="78" y="192">100</text><text x="78" y="246">80</text>
      <text x="78" y="300">60</text><text x="78" y="355">40</text><text x="78" y="409">20</text><text x="78" y="463">0</text>
    </g>
    <g fill="#1b1b1b">
      <rect x="110" y="188" width="14" height="271"/><rect x="185" y="215" width="14" height="244"/>
      <rect x="260" y="324" width="14" height="135"/><rect x="336" y="188" width="14" height="271"/>
      <rect x="411" y="188" width="14" height="271"/><rect x="486" y="296" width="14" height="163"/>
      <rect x="561" y="324" width="14" height="135"/>
    </g>
    <g fill="#0b5a8c">
      <rect x="132" y="215" width="14" height="244"/><rect x="207" y="242" width="14" height="217"/>
      <rect x="282" y="188" width="14" height="271"/><rect x="358" y="296" width="14" height="163"/>
      <rect x="433" y="215" width="14" height="244"/><rect x="508" y="256" width="14" height="203"/>
      <rect x="583" y="188" width="14" height="271"/>
    </g>
    <g fill="#222" text-anchor="middle" font-size="10.5">
      <text x="117" y="182">100</text><text x="139" y="209">90</text>
      <text x="192" y="209">90</text><text x="214" y="236">80</text>
      <text x="267" y="318">50</text><text x="289" y="182">100</text>
      <text x="343" y="182">100</text><text x="365" y="290">60</text>
      <text x="418" y="182">100</text><text x="440" y="209">90</text>
      <text x="493" y="290">60</text><text x="515" y="250">75</text>
      <text x="568" y="318">50</text><text x="590" y="182">100</text>
    </g>
    <g fill="#333" text-anchor="middle" font-weight="500" font-size="12">
      <text x="128" y="483">Sun</text><text x="204" y="483">Mon</text><text x="278" y="483">Tue</text>
      <text x="353" y="483">Wed</text><text x="428" y="483">Thu</text><text x="497" y="483">Fri</text><text x="569" y="483">Sat</text>
    </g>
  </svg>
  <h3 class="side-head"><span>The ultimate resort</span><br><span>experience</span></h3>
  <p class="side-copy">As the oldest continuously operating hotel in the Caribbean, The Heron Resort has had over a century to perfect luxury amenities and services expected by today's most discerning traveller. Our amenities range from cascading cliff-top pools and award-winning restaurants to an exciting kid's club and the spectacular Heron Beach - renowned as one of the most beautiful beaches in the world.</p>
  <footer class="footer">
    <div class="brand">The Heron</div>
    <div class="contact" style="left:310px"><svg viewBox="0 0 10 10"><path d="M2 0l2 2-1 1.5c.8 1.6 2 2.8 3.5 3.5L8 6l2 2-1.5 2C4 9.5.5 6 0 1.5z"/></svg>(246) 555-0142</div>
    <div class="sep" style="left:408px"></div>
    <div class="contact" style="left:423px"><svg viewBox="0 0 10 10"><path d="M0 2h10v6H0z"/></svg>reservations@theheronbay.example</div>
    <div class="sep" style="left:581px"></div>
    <div class="contact" style="left:595px"><svg viewBox="0 0 10 10"><circle cx="5" cy="5" r="5"/></svg>https://www.theheronbay.example/</div>
    <div class="page-label">Page</div><div class="page-div"></div><div class="page-num">02</div>
  </footer>
</section>

<!-- Slide 3: charts -->
<section class="slide" style="top:1403px">
  <div class="title-marker"></div>
  <h2 class="slide-title">Financial Charts</h2>
  <svg class="chart-svg" width="470" height="520" viewBox="0 0 470 520" font-family="Jost, sans-serif" font-size="24" fill="#fff">
    <g stroke="#fff" stroke-width="2">
      <path d="M256 307 L256 128 A179 179 0 1 1 160.1 458.1 Z" fill="#9dd3ef"/>
      <path d="M256 307 L160.1 458.1 A179 179 0 0 1 78.4 284.6 Z" fill="#58b0e0"/>
      <path d="M256 307 L78.4 284.6 A179 179 0 0 1 125.5 184.5 Z" fill="#0b5a8c"/>
      <path d="M256 307 L125.5 184.5 A179 179 0 0 1 256 128 Z" fill="#2a8fcf"/>
    </g>
    <text x="332" y="342" letter-spacing="1">59%</text>
    <text x="134" y="367" letter-spacing="1">18%</text>
    <text x="108" y="268" letter-spacing="1">10%</text>
    <text x="180" y="196" letter-spacing="1">13%</text>
  </svg>
  <div class="legend-item" style="top:119px">
    <div class="legend-icon" style="background:#0b5a8c"><svg viewBox="0 0 30 30"><path d="M5 25l8-8M10 10l10 10M18 5l7 7-5 5-7-7z"/></svg></div>
    <h3>LOREM IPSUM DOLOR (10%)</h3>
    <p>Lorem ipsum dolor sit amet, consectetur adipiscing elitsed do eiu tempor consectetur adipiscing incidiea.</p>
  </div>
  <div class="legend-item" style="top:221px">
    <div class="legend-icon" style="background:#1f88c8"><svg viewBox="0 0 30 30"><circle cx="15" cy="13" r="9"/><path d="M11 16v-3M15 16v-6M19 16v-4M6 26l4-5"/></svg></div>
    <h3>LOREM IPSUM DOLOR (13%)</h3>
    <p>Lorem ipsum dolor sit amet, consectetur adipiscing elitsed do eiu tempor consectetur adipiscing incidiea.</p>
  </div>
  <div class="legend-item" style="top:323px">
    <div class="legend-icon" style="background:#58b0e0"><svg viewBox="0 0 30 30"><circle cx="13" cy="13" r="6"/><path d="M17.5 17.5L25 25M13 3v3M13 20v3M3 13h3M20 13h3"/></svg></div>
    <h3>LOREM IPSUM DOLOR (18%)</h3>
    <p>Lorem ipsum dolor sit amet, consectetur adipiscing elitsed do eiu tempor consectetur adipiscing incidiea.</p>
  </div>
  <div class="legend-item" style="top:425px">
    <div class="legend-icon" style="background:#a8d8f2"><svg viewBox="0 0 30 30"><rect x="5" y="5" width="20" height="20" rx="2"/><path d="M9 11h12M9 15h8M9 19h10"/></svg></div>
    <h3>LOREM IPSUM DOLOR (59%)</h3>
    <p>Lorem ipsum dolor sit amet, consectetur adipiscing elitsed do eiu tempor consectetur adipiscing incidiea.</p>
  </div>
  <footer class="footer">
    <div class="brand">The Heron</div>
    <div class="contact" style="left:310px"><svg viewBox="0 0 10 10"><path d="M2 0l2 2-1 1.5c.8 1.6 2 2.8 3.5 3.5L8 6l2 2-1.5 2C4 9.5.5 6 0 1.5z"/></svg>(246) 555-0142</div>
    <div class="sep" style="left:408px"></div>
    <div class="contact" style="left:423px"><svg viewBox="0 0 10 10"><path d="M0 2h10v6H0z"/></svg>reservations@theheronbay.example</div>
    <div class="sep" style="left:581px"></div>
    <div class="contact" style="left:595px"><svg viewBox="0 0 10 10"><circle cx="5" cy="5" r="5"/></svg>https://www.theheronbay.example/</div>
    <div class="page-label">Page</div><div class="page-div"></div><div class="page-num">03</div>
  </footer>
</section>

<!-- Slide 4: tables -->
<section class="slide" style="top:2060px">
  <div class="title-marker"></div>
  <h2 class="slide-title">Financial Tables</h2>
  <table class="data-table">
    <thead><tr><th>THE HERON</th><th>RESORT</th><th>SUITES</th><th>DINING</th></tr></thead>
    <tbody>
      <tr><td>Lorem ipsum dolor</td><td>35%</td><td>8.5x</td><td>8.5x</td></tr>
      <tr><td>Sed ut perspea</td><td>48%</td><td>14.0x</td><td>14.0x</td></tr>
      <tr><td>Lorem ipsum dolor</td><td>12%</td><td>2.2x</td><td>2.2x</td></tr>
      <tr><td>Sed ut perspea</td><td>35%</td><td>6.5x</td><td>6.5x</td></tr>
      <tr><td>Lorem ipsum dolor</td><td>36%</td><td>5.8x</td><td>5.8x</td></tr>
      <tr><td>Sed ut perspea</td><td>96%</td><td>32.0x</td><td>32.0x</td></tr>
      <tr><td>Lorem ipsum dolor</td><td>33%</td><td>3.5x</td><td>3.5x</td></tr>
      <tr><td>Sed ut perspea</td><td>63%</td><td>7.7x</td><td>7.7x</td></tr>
      <tr><td>Lorem ipsum dolor</td><td>15%</td><td>1.7x</td><td>1.7x</td></tr>
      <tr><td>Sed ut perspea</td><td>21%</td><td>2.0x</td><td>2.0x</td></tr>
    </tbody>
  </table>
  <footer class="footer">
    <div class="brand">The Heron</div>
    <div class="contact" style="left:310px"><svg viewBox="0 0 10 10"><path d="M2 0l2 2-1 1.5c.8 1.6 2 2.8 3.5 3.5L8 6l2 2-1.5 2C4 9.5.5 6 0 1.5z"/></svg>(246) 555-0142</div>
    <div class="sep" style="left:408px"></div>
    <div class="contact" style="left:423px"><svg viewBox="0 0 10 10"><path d="M0 2h10v6H0z"/></svg>reservations@theheronbay.example</div>
    <div class="sep" style="left:581px"></div>
    <div class="contact" style="left:595px"><svg viewBox="0 0 10 10"><circle cx="5" cy="5" r="5"/></svg>https://www.theheronbay.example/</div>
    <div class="page-label">Page</div><div class="page-div"></div><div class="page-num">04</div>
  </footer>
</section>

<!-- Slide 5: gallery -->
<section class="slide" style="top:2718px">
  <div class="title-marker"></div>
  <h2 class="slide-title">Our Gallery</h2>
  <div class="photo" style="left:61px;top:102px;background:linear-gradient(180deg,#6fb0e0 0%,#a9d2ee 40%,#4d7d45 55%,#2f9fd1 75%,#6a6a66 100%)" role="img" aria-label="Poolside under an umbrella with tropical greenery"></div>
  <div class="photo" style="left:379px;top:102px;background:linear-gradient(180deg,#9aa8b4 0%,#b7c1c8 35%,#5a6e5a 55%,#6d6a60 75%,#8b8a82 100%)" role="img" aria-label="Wedding couple on a clifftop walkway by the sea"></div>
  <div class="photo" style="left:698px;top:102px;background:linear-gradient(180deg,#8fbfe3 0%,#e3e3de 35%,#c9c2b2 60%,#3fa9d2 80%,#b8b0a0 100%)" role="img" aria-label="Hotel building with loungers around a pool"></div>
  <div class="photo" style="left:61px;top:319px;background:linear-gradient(180deg,#6faee0 0%,#e9e9e6 40%,#d9d3c6 70%,#8fc8dc 100%)" role="img" aria-label="Private terrace with plunge pool and outdoor kitchen"></div>
  <div class="photo" style="left:379px;top:319px;background:linear-gradient(90deg,#4a2a22 0%,#5a2f25 25%,#9ec6df 45%,#3f8fb8 55%,#5a2f25 75%,#4a2a22 100%)" role="img" aria-label="Open wooden shutters framing an ocean view"></div>
  <div class="photo" style="left:698px;top:319px;background:linear-gradient(180deg,#e8e4dc 0%,#d9d2c4 45%,#f3f1ec 70%,#8a6d52 100%)" role="img" aria-label="Bright guest bedroom with sea view"></div>
  <footer class="footer">
    <div class="brand">The Heron</div>
    <div class="contact" style="left:310px"><svg viewBox="0 0 10 10"><path d="M2 0l2 2-1 1.5c.8 1.6 2 2.8 3.5 3.5L8 6l2 2-1.5 2C4 9.5.5 6 0 1.5z"/></svg>(246) 555-0142</div>
    <div class="sep" style="left:408px"></div>
    <div class="contact" style="left:423px"><svg viewBox="0 0 10 10"><path d="M0 2h10v6H0z"/></svg>reservations@theheronbay.example</div>
    <div class="sep" style="left:581px"></div>
    <div class="contact" style="left:595px"><svg viewBox="0 0 10 10"><circle cx="5" cy="5" r="5"/></svg>https://www.theheronbay.example/</div>
    <div class="page-label">Page</div><div class="page-div"></div><div class="page-num">05</div>
  </footer>
</section>

<!-- Slide 6: special occasions -->
<section class="slide" style="top:3375px">
  <div class="title-marker"></div>
  <h2 class="slide-title">Special Occasions</h2>
  <div class="feature-photo" role="img" aria-label="Guest relaxing in an infinity pool looking out to the sea and a jetty"></div>
  <ul class="features">
    <li>10 mins drive from Seawell Point International Airport</li>
    <li>40 acres of serene and tranquil environment providing several outdoor event venues with panoramic ocean views that are ideal for events</li>
    <li>Approximately 5,000 sq ft of indoor meeting/banqueting space</li>
    <li>Complimentary WiFi throughout the resort</li>
    <li>Complimentary local and international calls to most countries</li>
    <li>5 restaurants onsite, two of which have been top rated by Coastline Dining Guide</li>
    <li>Personalized service for a completely customized event experience</li>
  </ul>
  <footer class="footer">
    <div class="brand">The Heron</div>
    <div class="contact" style="left:310px"><svg viewBox="0 0 10 10"><path d="M2 0l2 2-1 1.5c.8 1.6 2 2.8 3.5 3.5L8 6l2 2-1.5 2C4 9.5.5 6 0 1.5z"/></svg>(246) 555-0142</div>
    <div class="sep" style="left:408px"></div>
    <div class="contact" style="left:423px"><svg viewBox="0 0 10 10"><path d="M0 2h10v6H0z"/></svg>reservations@theheronbay.example</div>
    <div class="sep" style="left:581px"></div>
    <div class="contact" style="left:595px"><svg viewBox="0 0 10 10"><circle cx="5" cy="5" r="5"/></svg>https://www.theheronbay.example/</div>
    <div class="page-label">Page</div><div class="page-div"></div><div class="page-num">06</div>
  </footer>
</section>

</body>
</html>
```